Design Podcast Artwork for a Leading Tech Company

Id like a a square piece of podcast cover artwork (1400x1400 pixels) designed for a new podcast Ive created for Venture Lantern, a leading tech investor based in Europe and Asia. The podcast is called Nine Quiet Builders and is about 4 entrepreneurs, discussing their experience building a company from scratch, including one who hasnt raised money yet (hence the 9 quiet builders title)
I need a square piece of artwork (1400x1400 pixels) that is:
A) Graphic based
B) That reflects the concept of Three and a Half
C) Follows the fonts and colour guidelines Ill give you
D) Includes the Title Nine Quiet Builders; the company name; By Venture Lantern and the company logo
Ive attached a piece of artwork from a previous podcast, Morning Ledger, Ive done for the company to give you a feel for the type of thing I want. A title, simple graphic, , By Venture Lantern; and the company logo which looks clean and professional. The company has since done a rebrand - hence the new colours and font - but they still want to convey a clean professionalism.
I have also attached a couple of samples from other designers that I wasnt entirely happy with for this podcast - I like that both tick all of the boxes above (Graphic based, reflect the concept of Three and a Half; follow font and colour guidelines etc.) but Im looking for fresh ideas and takes, so please be creative and come up with something fresh.
Hex codes for colours
Alabaster - white #F7F5F5
Aubergine - purple #2D1530
Peach - (for accents) #F8795D
Font
Rosario Bold
Look and feel

```html
<!DOCTYPE html>
<html lang="en">
<head>
<meta charset="utf-8">
<title>Nine Quiet Builders — Podcast Cover</title>
<link rel="stylesheet" href="https://fonts.googleapis.com/css2?family=Rosario:wght@400;700&display=swap">
<style>
  :root {
    --alabaster: #F7F5F5;
    --aubergine: #2D1530;
    --peach: #F8795D;
  }
  html, body {
    margin: 0;
    padding: 0;
    width: 1200px;
    height: 1200px;
    overflow: hidden;
    background: var(--alabaster);
  }
  .cover {
    position: relative;
    width: 1200px;
    height: 1200px;
    overflow: hidden;
    background: var(--alabaster);
    color: var(--aubergine);
    font-family: "Rosario", sans-serif;
  }
  .cover__numeral {
    position: absolute;
    left: -520px;
    top: -330px;
    margin: 0;
    font-family: "Rosario", sans-serif;
    font-weight: 700;
    font-size: 1700px;
    line-height: 1;
    color: var(--aubergine);
    user-select: none;
  }
  .cover__title {
    position: absolute;
    left: 424px;
    top: 290px;
    width: 690px;
    margin: 0;
    font-weight: 700;
    text-transform: uppercase;
  }
  .title__line {
    display: block;
    line-height: 1;
  }
  .title__line--lead {
    font-size: 214px;
    letter-spacing: 2px;
  }
  .title__line--middle {
    font-size: 150px;
    margin-top: 18px;
    display: flex;
    align-items: center;
    gap: 22px;
  }
  .title__rule {
    display: inline-block;
    width: 4px;
    height: 118px;
    background: var(--aubergine);
  }
  .title__line--sub {
    font-weight: 400;
    font-size: 96px;
    letter-spacing: 24px;
    margin-top: 26px;
  }
  .cover__brand {
    position: absolute;
    left: 560px;
    top: 930px;
    width: 440px;
    display: flex;
    align-items: center;
    justify-content: center;
    gap: 16px;
  }
  .brand__dot {
    width: 34px;
    height: 34px;
    border-radius: 50%;
    background: var(--aubergine);
  }
  .brand__name {
    font-weight: 700;
    font-size: 46px;
    color: var(--aubergine);
  }
  .cover__credit {
    position: absolute;
    left: 560px;
    top: 1060px;
    width: 440px;
    text-align: center;
    font-weight: 400;
    font-size: 25px;
    color: var(--aubergine);
  }
</style>
</head>
<body>
  <main class="cover">
    <div class="cover__numeral" aria-hidden="true">9</div>

    <h1 class="cover__title">
      <span class="title__line title__line--lead">Nine</span>
      <span class="title__line title__line--middle"><span class="title__rule"></span>Quiet</span>
      <span class="title__line title__line--sub">Builders</span>
    </h1>

    <div class="cover__brand">
      <span class="brand__dot"></span>
      <span class="brand__name">Venture Lantern</span>
    </div>

    <p class="cover__credit">By: Venture Lantern</p>
  </main>
</body>
</html>
```